Real Estate Investment Company Needs Business Card Design

TurnKeyDeal9 is a real estate investment company that primarily deals directly with homeowners looking to sell their homes in "as is" condition as quick as possible. We give this seller cash and close on their nightmare of a property in just a matter of days.

Our logo is attached - (please keep logo in tact, use as is)

Industry/Entity Type

Real Estate

Contact Information for Business Card

The design should invoke trust & professionalism. The person holding the card should feel rest assured that we are the right company to work with.

Font styles to use
Sans Serif

Requirements
Must have
• Card must include "Call us today for a fair offer on your property so you can move on with your life!"
Nice to have
• If possible, include this either on front or back (you can use your own formatting, below is just the text)
• "
• No Realtor Commissions
• No Repairs To Deal With
• No Closing Costs "

```html
<!DOCTYPE html>
<html lang="en">
<head>
<meta charset="utf-8">
<title>TurnKeyDeal9 Business Card</title>
<link rel="stylesheet" href="https://fonts.googleapis.com/css2?family=Lato:wght@700;900&display=swap">
<style>
  :root {
    --sky: #46bcf2;
    --paper: #ffffff;
    --ink: #1e2a33;
    --mark: #cfeefc;
  }
  html, body {
    margin: 0;
    padding: 0;
    width: 1200px;
    height: 720px;
    overflow: hidden;
    background: var(--sky);
  }
  .card {
    position: relative;
    width: 1200px;
    height: 720px;
    background: var(--sky);
  }
  .trim-marks {
    position: absolute;
    inset: 0;
  }
  .brand-band {
    position: absolute;
    left: 0;
    top: 225px;
    width: 1200px;
    height: 270px;
    background: var(--paper);
  }
  .brand-lockup {
    position: absolute;
    left: 0;
    right: 0;
    top: 160px;
    display: flex;
    align-items: center;
    justify-content: center;
    gap: 18px;
  }
  .brand-dot {
    width: 34px;
    height: 34px;
    border-radius: 50%;
    background: var(--sky);
  }
  .brand-name {
    font-family: "Lato", sans-serif;
    font-weight: 900;
    font-size: 60px;
    line-height: 1;
    letter-spacing: -0.5px;
    color: var(--ink);
  }
  .call-to-action {
    position: absolute;
    left: 60px;
    right: 60px;
    top: 585px;
    margin: 0;
    text-align: center;
    font-family: "Lato", sans-serif;
    font-weight: 700;
    font-size: 23px;
    line-height: 1.3;
    color: var(--paper);
  }
</style>
</head>
<body>
  <div class="card">
    <svg class="trim-marks" width="1200" height="720" viewBox="0 0 1200 720" aria-hidden="true">
      <g stroke="var(--mark)" stroke-width="1.5">
        <line x1="40" y1="0" x2="40" y2="20"/>
        <line x1="1160" y1="0" x2="1160" y2="20"/>
        <line x1="0" y1="40" x2="20" y2="40"/>
        <line x1="1180" y1="40" x2="1200" y2="40"/>
        <line x1="40" y1="700" x2="40" y2="720"/>
        <line x1="1160" y1="700" x2="1160" y2="720"/>
        <line x1="0" y1="680" x2="20" y2="680"/>
        <line x1="1180" y1="680" x2="1200" y2="680"/>
      </g>
    </svg>
    <div class="brand-band">
      <div class="brand-lockup">
        <span class="brand-dot"></span>
        <span class="brand-name">TurnKeyDeal9</span>
      </div>
    </div>
    <p class="call-to-action">Call us today for a fair offer on your property so you can move on with your life!</p>
  </div>
</body>
</html>
```